red quince
silk in motion
Modern
Dunmore Court
Harbor & Vale
Carmel, CA 93921
info@red-quince-shop.com
www.red-quince-shop.com
I'd like the card to be vertical, not horizontal! The logo should be centered!!!
should be the same, except the address:
P.O.Box 4819
Carmel, CA 93921-4819
logo should be centered on a vertical double sided business card!

```html
<!DOCTYPE html>
<html lang="en">
<head>
<meta charset="utf-8">
<title>Red Quince — stationery set</title>
<link rel="stylesheet" href="https://fonts.googleapis.com/css2?family=Quicksand:wght@400;500&display=swap">
<style>
  :root{
    --stage:#2a2b2d;
    --paper:#ffffff;
    --navy:#1d3f82;
    --navy-deep:#17346d;
    --cyan:#27a7df;
    --cyan-deep:#1f98cf;
    --cyan-light:#48b6e6;
    --sky:#c7e7f7;
    --mist:#e6f3fa;
    --ink:#4a5868;
    --label:#9aa0a6;
  }
  *{box-sizing:border-box;margin:0;padding:0}
  html,body{width:1200px;height:422px;overflow:hidden;background:var(--stage)}
  body{position:relative;font-family:"Quicksand",sans-serif;color:var(--ink)}

  .piece{position:absolute;background:var(--paper);overflow:hidden;box-shadow:0 2px 6px rgba(0,0,0,.55)}
  .piece svg.wave{position:absolute;left:0;bottom:0;width:100%}
  .caption{position:absolute;font-size:6px;color:var(--label);text-align:center;letter-spacing:.2px}

  .mark{display:flex;align-items:center;gap:4px;color:var(--navy);font-weight:500;white-space:nowrap}
  .mark .dot{border-radius:50%;background:var(--cyan);flex:none}

  /* business cards */
  .card{top:125px;width:53px;height:168px}
  .card-back{left:26px;background:var(--cyan)}
  .card-back .mark{position:absolute;left:0;right:0;top:78px;justify-content:center;color:var(--paper);font-size:7px}
  .card-back .mark .dot{width:6px;height:6px;background:var(--navy)}
  .card-front{left:84px}
  .card-front .mark{position:absolute;left:0;right:0;top:40px;justify-content:center;font-size:6.5px}
  .card-front .mark .dot{width:5px;height:5px}
  .card-front .details{position:absolute;left:0;right:0;top:62px;text-align:center;font-size:2.6px;line-height:4px}
  .card-front .details .tag{color:var(--cyan);font-size:3px}

  /* letterheads */
  .letterhead{top:29px;width:257px;height:355px}
  .letterhead.a{left:235px}
  .letterhead.b{left:528px}
  .letterhead .head{position:absolute;left:14px;top:14px;display:flex;gap:10px;align-items:flex-start}
  .letterhead .head .mark{font-size:8px}
  .letterhead .head .mark .dot{width:14px;height:14px}
  .letterhead .contact{font-size:3px;line-height:4.3px;padding-top:1px}
  .letterhead .backdrop{position:absolute;left:0;right:0;top:145px;text-align:center;font-size:34px;font-weight:400;color:var(--mist);white-space:nowrap}

  /* envelopes */
  .envelope{width:300px}
  .env-1{left:876px;top:67px;height:111px;background:var(--navy)}
  .env-2{left:876px;top:96px;height:101px;background:var(--cyan)}
  .env-3{left:833px;top:168px;height:113px}
  .env-4{left:816px;top:247px;height:118px}
  .envelope .flap{position:absolute;left:0;top:0;width:100%;height:100%}
  .envelope .mark{position:absolute;left:0;right:0;justify-content:center;font-size:6px}
  .envelope .mark .dot{width:6px;height:6px}
  .env-1 .mark{top:8px;color:var(--paper)}
  .env-2 .mark{top:10px;color:var(--paper)}
  .env-1 .mark .dot,.env-2 .mark .dot{background:var(--paper)}
  .env-3 .mark{top:24px}
  .env-4 .mark{top:44px}
  .envelope .return{position:absolute;left:0;right:0;text-align:center;font-size:2.6px;line-height:3.6px}
  .env-3 .return{top:35px}
  .env-4 .return{top:55px}
</style>
</head>
<body>

  <section class="piece card card-back" aria-label="Business card back">
    <div class="mark"><span class="dot"></span>Red Quince</div>
  </section>
  <p class="caption" style="left:26px;top:305px;width:53px">Back Card</p>

  <section class="piece card card-front" aria-label="Business card front">
    <div class="mark"><span class="dot"></span>Red Quince</div>
    <div class="details">
      <div class="tag">silk in motion</div>
      Dunmore Court<br>Harbor &amp; Vale<br>P.O.Box 4819<br>Carmel, CA 93921-4819<br><br>
      info@red-quince-shop.com<br>www.red-quince-shop.com
    </div>
    <svg class="wave" viewBox="0 0 53 14" height="14" preserveAspectRatio="none">
      <path d="M0 6 Q20 0 53 7 V14 H0Z" fill="var(--navy)"/>
      <path d="M0 9 Q25 3 53 10 V14 H0Z" fill="var(--cyan)"/>
    </svg>
  </section>
  <p class="caption" style="left:84px;top:305px;width:53px">Front Card</p>

  <section class="piece letterhead a" aria-label="Letterhead option A">
    <div class="head">
      <div class="mark"><span class="dot"></span>Red Quince</div>
      <div class="contact">Dunmore Court<br>Harbor &amp; Vale<br>P.O.Box 4819, Carmel, CA 93921-4819<br>info@red-quince-shop.com<br>www.red-quince-shop.com</div>
    </div>
    <div class="backdrop">Red Quince</div>
    <svg class="wave" viewBox="0 0 257 26" height="26" preserveAspectRatio="none">
      <path d="M0 10 Q90 -2 170 10 T257 6 V26 H0Z" fill="var(--sky)"/>
      <path d="M0 14 Q100 4 180 14 T257 10 V26 H0Z" fill="var(--navy)"/>
      <path d="M0 19 Q110 10 190 19 T257 15 V26 H0Z" fill="var(--cyan)"/>
    </svg>
  </section>
  <p class="caption" style="left:235px;top:391px;width:257px">Letterhead option A</p>

  <section class="piece letterhead b" aria-label="Letterhead option B">
    <div class="backdrop">Red Quince</div>
    <svg class="wave" viewBox="0 0 257 26" height="26" preserveAspectRatio="none">
      <path d="M0 10 Q90 -2 170 10 T257 6 V26 H0Z" fill="var(--sky)"/>
      <path d="M0 14 Q100 4 180 14 T257 10 V26 H0Z" fill="var(--navy)"/>
      <path d="M0 19 Q110 10 190 19 T257 15 V26 H0Z" fill="var(--cyan)"/>
    </svg>
  </section>
  <p class="caption" style="left:528px;top:391px;width:257px">Letterhead option B</p>

  <section class="piece envelope env-1" aria-label="Envelope back, navy">
    <svg class="flap" viewBox="0 0 300 111" preserveAspectRatio="none">
      <path d="M0 0 H300 L165 24 Q150 27 135 24Z" fill="var(--navy-deep)"/>
    </svg>
    <div class="mark"><span class="dot"></span>Red Quince</div>
  </section>

  <section class="piece envelope env-2" aria-label="Envelope back, cyan">
    <svg class="flap" viewBox="0 0 300 101" preserveAspectRatio="none">
      <path d="M0 0 H300 L165 40 Q150 44 135 40Z" fill="var(--cyan-deep)"/>
      <path d="M0 101 L140 58 Q150 55 160 58 L300 101Z" fill="var(--cyan-light)"/>
    </svg>
    <div class="mark"><span class="dot"></span>Red Quince</div>
  </section>

  <section class="piece envelope env-3" aria-label="Envelope front A">
    <div class="mark"><span class="dot"></span>Red Quince</div>
    <div class="return">P.O.Box 4819, Carmel, CA 93921-4819 · www.red-quince-shop.com</div>
  </section>

  <section class="piece envelope env-4" aria-label="Envelope front B">
    <div class="mark"><span class="dot"></span>Red Quince</div>
    <div class="return">P.O.Box 4819, Carmel, CA 93921-4819 · www.red-quince-shop.com</div>
    <svg class="wave" viewBox="0 0 300 16" height="16" preserveAspectRatio="none">
      <path d="M0 6 Q130 -2 300 7 V16 H0Z" fill="var(--navy)"/>
      <path d="M0 10 Q140 2 300 11 V16 H0Z" fill="var(--cyan)"/>
    </svg>
  </section>
  <p class="caption" style="left:816px;top:391px;width:300px">Envelope options</p>

</body>
</html>
```